Hochwertiges Plakat-Design für Konzert gesucht
Zielgruppe
Wir sind ein Konzertveranstalter und suchen ein hochwertiges Design für ein Konzertplakat. Unsere Zielgruppe sind Liebhaber der Filmmusik, eher Frauen im Alter 30+
Aufgabenstellung
Bei dem Projekt geht es um ein Konzertplakat - Format A0. Das Konzert hat den Titel GRAND CINEMA HEART SONGS, während des Konzertes wird die schönste und bekannteste Liebesmusik aus verschiedenen Filmen gespielt - live vom Halvor Ensemble in einer großen sinfonischen Besetzung.
GRAND CINEMA HEART SONGS
live mit dem Halvor Ensemble
Das Plakat soll auch die Namen der Komponisten - Teo Brask, Paul Kemble, Dario Pellavent, Victor Slade, Kurt Bellin - enthalten sowie separat einige Filmtitel: Unter kaltem Himmel, Rain Letters, Tobias und Mara, Coralwake, Hinter den Dünenfeldern, Midnight Steps, Schwur der Brandung, Fen Tide.
Außerdem muss das Plakat auch die Informationen enthalten, wo und wann das Konzertstattfindet:
Freitag, 10.01.2020, Magdeburg, Brückensaal
sowie die Ticketinformationen:
Billettstube im Markt-Galerie, Ernst-Reuter Allee 11, 39104 Magdeburg
und an allen bekannten VVK-Stallen
Onlinetickets saalkarten-online.de
Tickethotline: 0391-7046218
Die Informationen über das Datum und Ort sowie die Ticketinformationen müssen so gestaltet sein, dass man sie ersetzen kann, wenn das Konzert woanders stattfindet.

```html
<!DOCTYPE html>
<html lang="de">
<head>
<meta charset="utf-8">
<title>Grand Cinema Heart Songs – Konzertplakat</title>
<link rel="stylesheet" href="https://fonts.googleapis.com/css2?family=Jost:wght@500;600;700&display=swap">
<style>
  :root {
    --ink: #ffffff;
    --sky-top: #56636d;
    --sky-mid: #8a9ea8;
    --haze: #d8c0b2;
    --glow: #c98f82;
    --horizon: #7e4549;
    --ground: #2e2b31;
    --ground-deep: #1e1c21;
  }
  * { margin: 0; padding: 0; box-sizing: border-box; }
  html, body { width: 872px; height: 1200px; overflow: hidden; background: #ffffff; }
  .poster {
    position: relative;
    width: 872px;
    height: 1200px;
    overflow: hidden;
    font-family: "Jost", "Futura", sans-serif;
    color: var(--ink);
  }
  .poster__photo {
    position: absolute;
    inset: 0;
    background: linear-gradient(to bottom,
      var(--sky-top) 0%,
      #6d808a 18%,
      var(--sky-mid) 32%,
      var(--haze) 47%,
      var(--glow) 56%,
      var(--horizon) 62%,
      #4a3438 68%,
      var(--ground) 76%,
      var(--ground-deep) 100%);
  }
  .poster__type {
    position: absolute;
    inset: 0;
    width: 872px;
    height: 1200px;
  }
  .poster__type text {
    fill: var(--ink);
    font-family: "Jost", "Futura", sans-serif;
  }
  .headline { font-weight: 700; font-size: 132px; }
  .subline { font-weight: 600; font-size: 47px; }
  .side-list {
    position: absolute;
    top: 156px;
    writing-mode: vertical-rl;
    font-weight: 600;
    font-size: 19.5px;
    line-height: 27px;
    letter-spacing: 0.2px;
    text-transform: uppercase;
    white-space: nowrap;
  }
  .side-list--composers { left: 5px; }
  .side-list--films { right: 4px; }
  .ticket-info {
    position: absolute;
    top: 852px;
    left: 0;
    width: 872px;
    text-align: center;
    font-weight: 600;
    font-size: 19px;
    line-height: 27px;
    text-transform: uppercase;
  }
</style>
</head>
<body>
  <main class="poster">
    <div class="poster__photo" role="img" aria-label="Foto: Silhouette eines sich küssenden Paares mit Wunderkerze vor Abendhimmel in Dämmerungstönen"></div>

    <svg class="poster__type" viewBox="0 0 872 1200" aria-label="Titel und Termin">
      <text class="headline" x="2" y="96" textLength="868" lengthAdjust="spacingAndGlyphs">GRAND CINEMA</text>
      <text class="subline" x="2" y="139" textLength="868" lengthAdjust="spacingAndGlyphs">LIVE MIT DEM HALVOR ENSEMBLE</text>
      <text class="subline" x="3" y="1093" textLength="866" lengthAdjust="spacingAndGlyphs">FREITAG, 10.01.2020, BRÜCKENSAAL</text>
      <text class="headline" x="2" y="1197" textLength="868" lengthAdjust="spacingAndGlyphs">HEART SONGS</text>
    </svg>

    <p class="side-list side-list--composers">Teo Brask, Paul Kemble, Dario Pellavent, Victor Slade, Kurt Bellin</p>
    <p class="side-list side-list--films">Unter kaltem Himmel, Rain Letters, Tobias und Mara, Coralwake, Hinter den<br>Dünenfeldern, Midnight Steps, Schwur der Brandung, Fen Tide</p>

    <section class="ticket-info">
      <p>Billettstube im Markt-Galerie, Lindgrund-Weg 27,</p>
      <p>39112 Magdeburg</p>
      <p>und an allen bekannten VVK-Stallen</p>
      <p>Onlinetickets saalkarten-online.de</p>
      <p>Tickethotline: 0391-7046218</p>
    </section>
  </main>
</body>
</html>
```